New business stationairy

I need paper with header and footer and business cards.
I am a Ltd Company and my main field of expertise is QA/QC inspection in the Oil and Gas Industry. I will need all contact detail inserted and a footer with registration number and bank details etc

Industry/Entity Type

Business

```html
<!DOCTYPE html>
<html lang="en">
<head>
<meta charset="utf-8">
<title>Hartwell Verification Services – Business Cards</title>
<link href="https://fonts.googleapis.com/css2?family=Jost:wght@500&family=Roboto+Condensed:wght@400;700&display=swap" rel="stylesheet">
<style>
  :root {
    --brand: #0aa9e6;
    --band-light: #1fc2f0;
    --band-dark: #0097da;
    --backdrop-light: #a9a9a9;
    --backdrop-dark: #4f4f4f;
    --card: #ffffff;
    --page: #ffffff;
  }
  * { margin: 0; padding: 0; box-sizing: border-box; }
  html, body { width: 1200px; height: 1000px; overflow: hidden; background: var(--page); }
  .canvas { position: relative; width: 1200px; height: 1000px; }

  .presentation {
    position: absolute; left: 0; top: 0; width: 1200px; height: 809px;
    background: radial-gradient(ellipse 70% 75% at 50% 55%, var(--backdrop-light) 0%, #8a8a8a 45%, var(--backdrop-dark) 100%);
    border: 1px solid #3e3e3e;
  }

  .card {
    position: absolute; top: 236px; width: 460px; height: 283px;
    background: var(--card); overflow: hidden;
  }
  .card--front { left: 131px; }
  .card--back { left: 610px; }

  .wordmark { position: absolute; display: flex; align-items: center; color: var(--brand); font-family: "Jost", sans-serif; font-weight: 500; }
  .wordmark__square { background: var(--brand); border-radius: 4px; flex: none; }
  .wordmark__text { display: flex; flex-direction: column; }
  .wordmark__name { line-height: 1; letter-spacing: 0.5px; }
  .wordmark__sub { line-height: 1; }

  .card--front .wordmark { left: 110px; top: 77px; gap: 12px; }
  .card--front .wordmark__square { width: 50px; height: 50px; }
  .card--front .wordmark__name { font-size: 36px; }
  .card--front .wordmark__sub { font-size: 11px; margin-top: 3px; }

  .card--back .wordmark { left: 91px; top: 109px; gap: 12px; }
  .card--back .wordmark__square { width: 61px; height: 58px; }
  .card--back .wordmark__name { font-size: 39px; }
  .card--back .wordmark__sub { font-size: 12.5px; margin-top: 4px; }

  .contact-band {
    position: absolute; left: 0; bottom: 0; width: 100%; height: 104px;
    background: linear-gradient(90deg, var(--band-light) 0%, #06b3ea 45%, var(--band-dark) 100%);
    color: #fff; font-family: "Roboto Condensed", sans-serif;
  }
  .contact-band__block { position: absolute; top: 20px; font-size: 11px; line-height: 15px; }
  .contact-band__block strong { display: block; font-weight: 700; font-size: 11.5px; margin-bottom: 1px; }
  .contact-band__block--address { left: 50px; }
  .contact-band__block--person { left: 265px; }
  .contact-line { display: flex; align-items: center; gap: 3px; }
  .contact-line svg { width: 9px; height: 9px; flex: none; }

  .wordmark--large { left: 145px; top: 869px; gap: 16px; }
  .wordmark--large .wordmark__square { width: 82px; height: 80px; border-radius: 6px; }
  .wordmark--large .wordmark__name { font-size: 56px; }
  .wordmark--large .wordmark__sub { font-size: 17px; margin-top: 5px; }
</style>
</head>
<body>
<div class="canvas">
  <section class="presentation">
    <article class="card card--front">
      <div class="wordmark">
        <span class="wordmark__square"></span>
        <span class="wordmark__text">
          <span class="wordmark__name">HARTWELL</span>
          <span class="wordmark__sub">Verification Services . Ltd</span>
        </span>
      </div>
      <div class="contact-band">
        <div class="contact-band__block contact-band__block--address">
          <strong>Willow House</strong>
          Mill Road, Ashcombe, Northfield,<br>
          Somerset, TA4 9QX.
        </div>
        <div class="contact-band__block contact-band__block--person">
          <strong>Helen Hartwell</strong>
          <span class="contact-line">
            <svg viewBox="0 0 10 10"><circle cx="5" cy="5" r="5" fill="#fff"/><rect x="2.3" y="3.2" width="5.4" height="3.6" fill="none" stroke="#0aa9e6" stroke-width="0.9"/><path d="M2.3 3.3 5 5.3 7.7 3.3" fill="none" stroke="#0aa9e6" stroke-width="0.8"/></svg>
            hello@hartwellvs.co.uk
          </span>
          <span class="contact-line">
            <svg viewBox="0 0 10 10"><circle cx="5" cy="5" r="5" fill="#fff"/><path d="M3 2.6c.4-.3.8-.2 1 .2l.4.8c.1.3 0 .5-.2.7l-.3.2c.3.6.7 1 1.3 1.3l.2-.3c.2-.2.4-.3.7-.2l.8.4c.4.2.5.6.2 1-.4.6-1 .8-1.7.5C4.5 6.7 3.3 5.5 2.8 4.3c-.3-.7-.2-1.3.2-1.7z" fill="#0aa9e6"/></svg>
            07700 900418
          </span>
        </div>
      </div>
    </article>

    <article class="card card--back">
      <div class="wordmark">
        <span class="wordmark__square"></span>
        <span class="wordmark__text">
          <span class="wordmark__name">HARTWELL</span>
          <span class="wordmark__sub">Verification Services . Ltd</span>
        </span>
      </div>
    </article>
  </section>

  <div class="wordmark wordmark--large">
    <span class="wordmark__square"></span>
    <span class="wordmark__text">
      <span class="wordmark__name">HARTWELL</span>
      <span class="wordmark__sub">Verification Services . Ltd</span>
    </span>
  </div>
</div>
</body>
</html>
```